Velnora - Quality health delivered at your door

Velnora offers home and Community Based Services for adults who wish to continue live independently in their communities. We increase accessibility to health care, reduce health care delivery gap, reduce mortality and morbidity, reduce health while promoting healthy living in the comfort of our patients communities or homes.

We provide on site services and deliver high quality healthcare at your door. Our experienced physicians coordinate care with our certified nurse practitioners and provide chronic care management, physical therapy, rehabilitation and medications management.

Target Market(s)

Older population living in independent living facilities

Industry/Entity Type

Health Care

Contact Information for Business Card

Velnora

Number of Pages Required

4 page

Font styles to use
Sans Serif

Colors

Designer to choose colors to be used in the design.

```html
<!DOCTYPE html>
<html lang="en">
<head>
<meta charset="utf-8">
<title>Velnora - Quality health delivered at your door</title>
<link href="https://fonts.googleapis.com/css2?family=Roboto:wght@300;400;500;700;900&family=Oswald:wght@500;600&display=swap" rel="stylesheet">
<style>
:root{
  --orange:#f7941d;
  --orange-dark:#d87b0c;
  --orange-field:#c9730f;
  --green:#5b7f1f;
  --green-dark:#4a6a17;
  --ink:#222222;
  --text:#555555;
  --muted:#8a8a8a;
  --light:#f3f3f3;
  --white:#ffffff;
  --footer:#1f1f1f;
  --footer-bar:#151515;
}
*{box-sizing:border-box;margin:0;padding:0}
html,body{width:1200px;height:3352px;overflow:hidden}
body{position:relative;font-family:'Roboto',Arial,sans-serif;color:var(--text);background:var(--white)}
.abs{position:absolute}
.img-fill{position:absolute}

/* header */
.site-header{position:absolute;left:0;top:0;width:1200px;height:95px;z-index:5}
.brand{position:absolute;left:150px;top:14px;display:flex;flex-direction:column;align-items:center}
.brand-dot{width:44px;height:44px;border-radius:50%;background:var(--orange)}
.brand-name{font:700 17px 'Roboto',sans-serif;color:var(--green);letter-spacing:.5px;margin-top:4px}
.contact{position:absolute;top:18px;display:flex;gap:8px;align-items:flex-start;font-size:10px;color:var(--ink)}
.contact b{display:block;color:var(--orange);font-weight:500;font-size:11px}
.contact svg{flex:none}
.header-social{position:absolute;left:896px;top:18px;display:flex;gap:6px}
.header-social span{width:22px;height:22px;border-radius:50%;border:1.5px solid var(--orange)}
.main-nav{position:absolute;left:340px;top:63px;display:flex;gap:17px;font-size:10.5px;color:var(--orange)}
.main-nav a{color:var(--orange);text-decoration:none}
.main-nav a.active{color:var(--ink)}

/* hero */
.hero{position:absolute;left:0;top:0;width:1200px;height:632px;background:linear-gradient(100deg,#efe6d6 0%,#f6f0e4 35%,#d9c7ac 60%,#c9b292 80%,#efe3cf 100%)}
.welcome{position:absolute;left:96px;top:198px;width:420px;height:380px}
.welcome-text{position:absolute;left:68px;top:58px;width:300px;color:var(--white)}
.welcome-text h1{font:900 42px/42px 'Roboto',sans-serif;letter-spacing:-.5px}
.welcome-text .rule{height:1px;background:rgba(255,255,255,.5);margin:14px 0 12px;width:290px}
.welcome-text p{font-size:14px;line-height:19px}
.btn{display:inline-block;background:var(--orange);color:var(--white);font:500 12px 'Roboto',sans-serif;border-radius:20px;padding:10px 0;width:132px;text-align:center}
.welcome-text .btn{margin-top:14px}

/* about */
.about-card{position:absolute;left:245px;top:677px;width:360px;height:235px;background:var(--white);box-shadow:0 2px 10px rgba(0,0,0,.15);padding:18px 20px}
.about-card h2{font:700 28px 'Roboto',sans-serif;color:var(--orange)}
.about-card .lead{font-size:13px;line-height:16px;color:var(--text);margin-top:4px}
.about-card .body{font-size:9.5px;line-height:14px;color:var(--text);margin-top:10px}
.about-card .body p+p{margin-top:8px}
.about-card .btn{margin-top:12px;width:128px;padding:9px 0}
.heart{position:absolute;right:40px;top:90px}
.about-photo{left:628px;top:677px;width:324px;height:295px;background:linear-gradient(135deg,#e8e4ea,#b8b2c2 50%,#7a3048 75%,#c64a4a)}

/* services */
.services-band{left:0;top:1000px;width:1200px;height:540px}
.section-title{position:absolute;width:1200px;text-align:center;font:700 44px 'Roboto',sans-serif;color:var(--white);letter-spacing:.5px}
.section-sub{position:absolute;width:1200px;text-align:center;font:300 16px 'Roboto',sans-serif;color:rgba(255,255,255,.8)}
.service-card{position:absolute;width:219px;height:172px;background:var(--white);box-shadow:0 2px 8px rgba(0,0,0,.15);text-align:center;padding-top:18px}
.service-icon{width:78px;height:78px;border-radius:50%;background:var(--orange);margin:0 auto;display:flex;align-items:center;justify-content:center;color:var(--white);font:700 44px 'Roboto',sans-serif}
.service-card h3{font:700 11px 'Roboto',sans-serif;color:var(--ink);margin-top:14px}
.service-card p{font-size:9.5px;line-height:13px;color:var(--muted);margin:6px 22px 0}

/* why us */
.why{left:0;top:1540px;width:1200px;height:470px;background:linear-gradient(180deg,#f2f2f2,#fafafa)}
.why h2{position:absolute;left:54px;top:56px;font:900 46px/44px 'Roboto',sans-serif;color:var(--green)}
.why .lead{position:absolute;left:54px;top:155px;font-size:18px;color:var(--ink)}
.why .body{position:absolute;left:54px;top:190px;width:430px;font-size:9.5px;line-height:15px;color:var(--text)}
.checks{position:absolute;left:54px;top:288px;display:grid;grid-template-columns:190px 240px;row-gap:20px;font-size:12px;color:var(--ink)}
.checks li{list-style:none;display:flex;align-items:center;gap:12px}
.why-photo{left:572px;top:1548px;width:600px;height:460px}

/* faq + appointment */
.faq{position:absolute;left:248px;top:2056px;width:322px}
.faq h2{font:700 21px 'Roboto',sans-serif;color:var(--orange)}
.faq-item{display:flex;align-items:center;gap:12px;font-size:10.5px;color:var(--text);border-bottom:1px solid #e3e3e3;padding:10px 0}
.faq-item .ring{width:14px;height:14px;border-radius:50%;border:1px solid #999;display:flex;align-items:center;justify-content:center;font-size:11px;line-height:1;color:#777;flex:none}
.faq-answer{font-size:9.5px;line-height:14px;color:var(--text);padding:14px 0;border-bottom:1px solid #e3e3e3}
.appointment{position:absolute;left:604px;top:2060px;width:346px;height:275px;background:var(--orange);border:6px solid #fbe7cf;box-shadow:0 2px 10px rgba(0,0,0,.2);padding:18px 16px}
.appointment h2{font:700 21px 'Roboto',sans-serif;color:var(--white);text-align:center}
.field{position:absolute;background:var(--orange-field);color:var(--white);font-size:10px;padding:10px 12px}
.appointment .note{position:absolute;left:22px;top:222px;font:700 9.5px 'Roboto',sans-serif;color:var(--white)}
.appointment .submit{position:absolute;left:174px;top:206px;width:148px;height:40px;background:var(--white);color:var(--orange);font:500 12px/40px 'Roboto',sans-serif;text-align:center}

/* blogs */
.blogs{left:0;top:2380px;width:1200px;height:575px;background:linear-gradient(180deg,#f5f5f5,#ececec)}
.blogs .section-title{color:var(--orange);top:2416px}
.blogs-sub{top:2476px;color:rgba(247,148,29,.55)}
.blog-card{position:absolute;top:2521px;width:283px;height:369px;background:var(--white);box-shadow:0 2px 8px rgba(0,0,0,.15)}
.blog-photo{position:absolute;left:6px;top:6px;width:271px;height:192px}
.blog-date{position:absolute;left:6px;top:198px;background:var(--orange);color:var(--white);font-size:10.5px;padding:4px 12px}
.blog-card h3{position:absolute;left:14px;top:234px;font:500 18px 'Roboto',sans-serif;color:var(--ink)}
.blog-card p{position:absolute;left:14px;top:264px;width:255px;font-size:9.5px;line-height:13px;color:var(--text)}
.blog-card .btn{position:absolute;left:14px;top:312px;width:110px;padding:9px 0}

/* social band + footer */
.social-band{left:0;top:2955px;width:1200px;height:85px;background:var(--green)}
.social-row{position:absolute;left:0;top:2974px;width:1200px;display:flex;justify-content:center;gap:22px}
.social-row span{width:50px;height:50px;border-radius:50%;border:2px solid var(--white)}
.site-footer{left:0;top:3040px;width:1200px;height:278px;background:var(--footer);color:#e0e0e0}
.footer-col{position:absolute;top:3070px}
.footer-col h4{font:500 20px 'Oswald',sans-serif;color:var(--white);letter-spacing:.5px}
.footer-col p{font-size:9.5px;line-height:13px;margin-top:16px}
.footer-col ul{list-style:none;margin-top:12px;font-size:10px}
.footer-col li{margin-bottom:13px}
.footer-col li::before{content:"› ";}
.f-contact{display:flex;gap:8px;align-items:flex-start;font-size:9.5px;line-height:13px;margin-top:12px}
.insta{display:grid;grid-template-columns:repeat(3,50px);gap:6px;margin-top:16px}
.insta span{height:38px}
.newsletter-input{margin-top:16px;width:215px;height:32px;border-radius:16px;background:var(--white);color:#888;font-size:9.5px;line-height:32px;padding-left:20px}
.newsletter-btn{margin-top:12px;width:126px;height:30px;border-radius:15px;background:var(--orange);color:var(--white);font:700 12px/30px 'Roboto',sans-serif;text-align:center}
.footer-bar{left:0;top:3318px;width:1200px;height:34px;background:var(--footer-bar);color:#bbb;font-size:10px;line-height:34px;padding-left:152px}
.footer-bar b{color:var(--orange);font-weight:500}
</style>
</head>
<body>

<!-- hero -->
<div class="hero" role="img" aria-label="Photo of an elderly couple at home talking with a caregiver"></div>

<header class="site-header">
  <div class="brand"><span class="brand-dot"></span><span class="brand-name">VELNORA</span></div>
  <div class="contact" style="left:346px">
    <svg width="20" height="20" viewBox="0 0 24 24"><path fill="#f7941d" d="M6.6 10.8a15.1 15.1 0 0 0 6.6 6.6l2.2-2.2c.3-.3.7-.4 1-.2 1.1.4 2.3.6 3.6.6.6 0 1 .4 1 1V20c0 .6-.4 1-1 1A17 17 0 0 1 3 4c0-.6.4-1 1-1h3.5c.6 0 1 .4 1 1 0 1.3.2 2.5.6 3.6.1.3 0 .7-.2 1z"/></svg>
    <div><b>Phone Number :</b>000.000.000</div>
  </div>
  <div class="contact" style="left:508px">
    <svg width="24" height="18" viewBox="0 0 24 18"><rect x="1" y="1" width="22" height="16" rx="1" fill="#f7941d"/><path d="M1 2l11 8 11-8" stroke="#fff" stroke-width="1.6" fill="none"/></svg>
    <div><b>Email Address :</b>info@velnora.com</div>
  </div>
  <div class="contact" style="left:688px">
    <svg width="18" height="24" viewBox="0 0 18 24"><path fill="#f7941d" d="M9 0a9 9 0 0 1 9 9c0 6-9 15-9 15S0 15 0 9a9 9 0 0 1 9-9z"/><circle cx="9" cy="9" r="3.5" fill="#fff"/></svg>
    <div><b>Address :</b>Lorem Ipsum is simply dummy</div>
  </div>
  <div class="header-social"><span></span><span></span><span></span><span></span><span></span></div>
  <nav class="main-nav">
    <a class="active">Home</a><a>Assisted Living</a><a>Skilled Nursing</a><a>Independent Living</a><a>Community Based Services</a><a>Respite Care</a><a>Rehabilitation</a><a>Kestrel Learning Center</a><a>Kestrel Learning</a>
  </nav>
</header>

<div class="welcome">
  <svg width="420" height="380" viewBox="0 0 420 380">
    <path d="M60 8 H340 Q410 8 410 80 V250 Q410 300 360 315 L360 372 L300 320 H70 Q8 320 8 250 V80 Q8 8 60 8 Z" fill="#f7941d"/>
    <path d="M62 20 H336 Q398 20 398 82 V246 Q398 290 352 304 L352 346 L304 308 H72 Q20 308 20 246 V82 Q20 20 62 20 Z" fill="#5b7f1f"/>
  </svg>
  <div class="welcome-text">
    <h1>WELCOME TO<br>VELNORA</h1>
    <div class="rule"></div>
    <p>Velnora offers home and Community Based Services for adults who wish to continue to live independently in the comfort of their communities</p>
    <span class="btn">Read More</span>
  </div>
  <svg class="abs" style="left:340px;top:152px" width="20" height="18" viewBox="0 0 24 22"><path fill="#f7941d" d="M12 21 2.5 11.5a5.5 5.5 0 0 1 9.5-6 5.5 5.5 0 0 1 9.5 6z"/></svg>
</div>

<!-- about -->
<section class="about-card">
  <h2>ABOUT VELNORA</h2>
  <p class="lead">Lorem Ipsum is simply dummy text of the printing and typesetting industry.</p>
  <svg class="heart" width="18" height="16" viewBox="0 0 24 22"><path fill="#f7941d" d="M12 21 2.5 11.5a5.5 5.5 0 0 1 9.5-6 5.5 5.5 0 0 1 9.5 6z"/></svg>
  <div class="body">
    <p>Velnora offers home and Community Based Services for adults who wish to continue to live independently in the comfort of their communities.</p>
    <p>We provide on site services and deliver high quality healthcare at your door. Our experienced physicians coordinate care with our certified nurse practitioners and provide chronic care management, physical therapy, rehabilitation and medications management</p>
  </div>
  <span class="btn">Read More</span>
</section>
<div class="img-fill about-photo" role="img" aria-label="Photo of a nurse and visitor with an elderly man in a wheelchair"></div>

<!-- services -->
<svg class="img-fill services-band" viewBox="0 0 1200 540" role="img" aria-label="Photo of caregivers and patients under an orange tint">
  <defs>
    <linearGradient id="svcTint" x1="0" x2="1">
      <stop offset="0" stop-color="#e98a12"/><stop offset=".5" stop-color="#f7a12e"/><stop offset="1" stop-color="#ec8c14"/>
    </linearGradient>
  </defs>
  <path d="M0 20 Q600 -20 1200 20 V510 Q600 560 0 510 Z" fill="url(#svcTint)"/>
</svg>
<h2 class="section-title" style="top:1040px">OUR SERVICES</h2>
<p class="section-sub" style="top:1090px">Lorem Ipsum is simply dummy text of the printing and typesetting industry.</p>

<div class="service-card" style="left:257px;top:1128px">
  <div class="service-icon"><svg width="38" height="30" viewBox="0 0 38 30"><path d="M3 15l11 11L35 4" stroke="#fff" stroke-width="5" fill="none"/></svg></div>
  <h3>HOME HEALTH ASSISTANCE</h3><p>Lorem Ipsum is simply dummy text of the printing and typesetting industry.</p>
</div>
<div class="service-card" style="left:492px;top:1128px">
  <div class="service-icon">?</div>
  <h3>MENTAL HEALTH</h3><p>Lorem Ipsum is simply dummy text of the printing and typesetting industry.</p>
</div>
<div class="service-card" style="left:726px;top:1128px">
  <div class="service-icon">$</div>
  <h3>PHYSICAL THERAPY</h3><p>Lorem Ipsum is simply dummy text of the printing and typesetting industry.</p>
</div>
<div class="service-card" style="left:257px;top:1314px">
  <div class="service-icon"><svg width="30" height="40" viewBox="0 0 18 24"><path fill="#fff" d="M9 0a9 9 0 0 1 9 9c0 6-9 15-9 15S0 15 0 9a9 9 0 0 1 9-9z"/><circle cx="9" cy="9" r="3.5" fill="#f7941d"/></svg></div>
  <h3>TRANSITIONAL CARE</h3><p>Lorem Ipsum is simply dummy text of the printing and typesetting industry.</p>
</div>
<div class="service-card" style="left:492px;top:1314px">
  <div class="service-icon" style="font-style:italic;font-family:Georgia,serif">i</div>
  <h3>TRANSPORTATION</h3><p>Lorem Ipsum is simply dummy text of the printing and typesetting industry.</p>
</div>
<div class="service-card" style="left:726px;top:1314px">
  <div class="service-icon"><svg width="38" height="32" viewBox="0 0 38 32"><rect x="2" y="7" width="34" height="23" rx="3" fill="#fff"/><rect x="13" y="2" width="12" height="7" rx="2" fill="none" stroke="#fff" stroke-width="3"/><path d="M19 12v13M12.5 18.5h13" stroke="#f7941d" stroke-width="4"/></svg></div>
  <h3>DENTAL HEALTH</h3><p>Lorem Ipsum is simply dummy text of the printing and typesetting industry.</p>
</div>

<!-- why us -->
<section class="abs why">
  <h2>WHY US<br>VELNORA?</h2>
  <p class="lead">Lorem Ipsum is simply dummy text of the printing</p>
  <p class="body">Lorem Ipsum is simply dummy text of the printing and typesetting industry. Lorem Ipsum has been the industry's standard dummy text ever since the 1500s, when an unknown printer took a galley of type and scrambled it to make a type specimen book. It has survived not only five centuries, but also the leap into electronic typesetting, remaining essentially unchanged. It was popularised in the 1960s with the release of Letraset sheets containing Lorem Ipsum passages.</p>
  <ul class="checks">
    <li><svg width="18" height="18" viewBox="0 0 18 18"><circle cx="9" cy="9" r="8" fill="none" stroke="#5b7f1f" stroke-width="1.4"/><path d="M5 9l3 3 5-6" stroke="#5b7f1f" stroke-width="1.6" fill="none"/></svg>Physical therapy</li>
    <li><svg width="18" height="18" viewBox="0 0 18 18"><circle cx="9" cy="9" r="8" fill="none" stroke="#5b7f1f" stroke-width="1.4"/><path d="M5 9l3 3 5-6" stroke="#5b7f1f" stroke-width="1.6" fill="none"/></svg>Comprehensive primary care services</li>
    <li><svg width="18" height="18" viewBox="0 0 18 18"><circle cx="9" cy="9" r="8" fill="none" stroke="#5b7f1f" stroke-width="1.4"/><path d="M5 9l3 3 5-6" stroke="#5b7f1f" stroke-width="1.6" fill="none"/></svg>Mental health</li>
    <li><svg width="18" height="18" viewBox="0 0 18 18"><circle cx="9" cy="9" r="8" fill="none" stroke="#5b7f1f" stroke-width="1.4"/><path d="M5 9l3 3 5-6" stroke="#5b7f1f" stroke-width="1.6" fill="none"/></svg>Coordination of speciality care</li>
  </ul>
</section>
<svg class="img-fill why-photo" viewBox="0 0 600 460" role="img" aria-label="Photo of a smiling nurse with an elderly man reading a book">
  <defs>
    <linearGradient id="whyPhoto" x1="0" y1="0" x2="1" y2="1">
      <stop offset="0" stop-color="#f2eeea"/><stop offset=".5" stop-color="#d9cbbd"/><stop offset="1" stop-color="#8f8274"/>
    </linearGradient>
  </defs>
  <circle cx="300" cy="222" r="316" fill="url(#whyPhoto)"/>
  <circle cx="300" cy="222" r="316" fill="none" stroke="#5b7f1f" stroke-width="18"/>
</svg>

<!-- faq -->
<section class="faq">
  <h2>FREQUENTLY ASKED QUESTIONS</h2>
  <div style="height:14px;border-bottom:1px solid #e3e3e3"></div>
  <div class="faq-item"><span class="ring">–</span>Comprehensive primary care services?</div>
  <div class="faq-answer">Lorem Ipsum is simply dummy text of the printing and typesetting industry. Lorem Ipsum has been the industry's standard dummy text ever since the 1500s, when an unknown printer took a galley of type and scrambled it to make a type specimen book</div>
  <div class="faq-item"><span class="ring">+</span>Coordination of speciality care?</div>
  <div class="faq-item"><span class="ring">+</span>Chronic disease management such as COPD, Asthma ?</div>
  <div class="faq-item"><span class="ring">+</span>Social services assessment ?</div>
</section>

<section class="appointment">
  <h2>MAKE AN APPOINTMENT</h2>
  <div class="field" style="left:20px;top:64px;width:146px;height:36px">Your Name</div>
  <div class="field" style="left:20px;top:110px;width:146px;height:36px">Your Email</div>
  <div class="field" style="left:20px;top:156px;width:146px;height:36px">Your Subject</div>
  <div class="field" style="left:176px;top:64px;width:146px;height:128px">Your Messages</div>
  <p class="note">ALL FIELDS ARE OBLIGATORY</p>
  <div class="submit">Make An Appointment</div>
</section>

<!-- blogs -->
<section class="abs blogs"></section>
<h2 class="section-title" style="color:var(--orange);top:2418px">LATEST BLOGS</h2>
<p class="section-sub blogs-sub" style="top:2476px;color:rgba(247,148,29,.6)">Lorem Ipsum is simply dummy text of the printing and typesetting industry</p>

<article class="blog-card" style="left:152px">
  <div class="blog-photo" role="img" aria-label="Photo of a caregiver with an elderly couple at a table" style="background:linear-gradient(135deg,#d8cfc5,#b7443a 55%,#5d6f9a)"></div>
  <span class="blog-date">15 AUG 2017</span>
  <h3>Top 28 Best Healthy Snacks</h3>
  <p>Lorem Ipsum is simply dummy text of the printing and typesetting industry. Lorem Ipsum has been the industry's standard dummy text ever since the 1500s.</p>
  <span class="btn">Read More</span>
</article>
<article class="blog-card" style="left:458px">
  <div class="blog-photo" role="img" aria-label="Photo of a group support session" style="background:linear-gradient(135deg,#e8d8b8,#c6b08a 50%,#4f9a8a)"></div>
  <span class="blog-date">15 AUG 2017</span>
  <h3>Top 28 Best Healthy Snacks</h3>
  <p>Lorem Ipsum is simply dummy text of the printing and typesetting industry. Lorem Ipsum has been the industry's standard dummy text ever since the 1500s.</p>
  <span class="btn">Read More</span>
</article>
<article class="blog-card" style="left:764px">
  <div class="blog-photo" role="img" aria-label="Photo of a counsellor talking with a patient" style="background:linear-gradient(135deg,#f4f2ef,#e2dcd6 50%,#b8b0a8)"></div>
  <span class="blog-date">15 AUG 2017</span>
  <h3>Top 28 Best Healthy Snacks</h3>
  <p>Lorem Ipsum is simply dummy text of the printing and typesetting industry. Lorem Ipsum has been the industry's standard dummy text ever since the 1500s.</p>
  <span class="btn">Read More</span>
</article>

<!-- social band -->
<div class="abs social-band"></div>
<div class="social-row"><span></span><span></span><span></span><span></span><span></span></div>

<!-- footer -->
<footer class="abs site-footer"></footer>
<div class="footer-col" style="left:152px;width:210px">
  <h4>VELNORA</h4>
  <p>Lorem Ipsum is simply dummy text of the printing and typesetting industry. Lorem Ipsum has been the industry's standard dummy text ever since the 1500s</p>
  <div class="f-contact"><svg width="12" height="12" viewBox="0 0 24 24"><path fill="#ddd" d="M6.6 10.8a15.1 15.1 0 0 0 6.6 6.6l2.2-2.2c.3-.3.7-.4 1-.2 1.1.4 2.3.6 3.6.6.6 0 1 .4 1 1V20c0 .6-.4 1-1 1A17 17 0 0 1 3 4c0-.6.4-1 1-1h3.5c.6 0 1 .4 1 1 0 1.3.2 2.5.6 3.6.1.3 0 .7-.2 1z"/></svg>000.000.000</div>
  <div class="f-contact"><svg width="13" height="10" viewBox="0 0 24 18"><rect x="1" y="1" width="22" height="16" fill="none" stroke="#ddd" stroke-width="2"/><path d="M1 2l11 8 11-8" stroke="#ddd" stroke-width="2" fill="none"/></svg>info@velnora.com</div>
  <div class="f-contact"><svg width="10" height="13" viewBox="0 0 18 24"><path fill="#ddd" d="M9 0a9 9 0 0 1 9 9c0 6-9 15-9 15S0 15 0 9a9 9 0 0 1 9-9z"/></svg>Lorem Ipsum is simply dummy text of the<br>printing and typesetting industry</div>
</div>
<div class="footer-col" style="left:425px">
  <h4>QUICK LINK</h4>
  <ul><li>Home</li><li>About us</li><li>Services</li><li>Blog</li><li>Contact us</li></ul>
</div>
<div class="footer-col" style="left:581px">
  <h4>INSTAGRAM PHOTOS</h4>
  <div class="insta" role="img" aria-label="Grid of nine small care photos">
    <span style="background:#b9a58e"></span><span style="background:#c9866e"></span><span style="background:#d8d2cc"></span>
    <span style="background:#8e9bb0"></span><span style="background:#c6a17c"></span><span style="background:#a4785e"></span>
    <span style="background:#d3b99a"></span><span style="background:#9aa884"></span><span style="background:#c8c0b6"></span>
  </div>
</div>
<div class="footer-col" style="left:809px">
  <h4>NEWSLETTER</h4>
  <p>Lorem Ipsum is simply dummy text of the printing and typesetting industry. Lorem Ipsum has been the industry's standard dummy text ever since the 1500s</p>
  <div class="newsletter-input">Your Email Address</div>
  <div class="newsletter-btn">Send</div>
</div>
<div class="abs footer-bar">Copyright © 2017 <b>Velnora</b>. All Rights Reserved.</div>

</body>
</html>
```